Business Card redesign

we are electricians i need a modern professional double side business card using my current branding=g

The card information must have site address~ 17 Pellow st cobram, Vic 3644 postal address~ P.o. Box 762 cobram,Vic 3643 Phone Number~0358916047 Fax Nunber~0358934268 Email address~ kierant@vorpelt.com.au Title~ Manager Licence numbers~ Vic 27584, NSW 41958K,Solar B3168459 Web site~ www.vorpelt.com.au

Industry/Entity Type

Business

```html
<!DOCTYPE html>
<html lang="en">
<head>
<meta charset="utf-8">
<title>Vorpelt Pty. Ltd. – Business Card</title>
<link rel="stylesheet" href="https://fonts.googleapis.com/css2?family=Raleway:wght@400;500;700;800&display=swap">
<style>
  :root {
    --page-bg: #e4e5e7;
    --card-bg: #ffffff;
    --brand-navy: #2e3192;
    --brand-red: #e31e24;
    --name-grey: #858585;
    --ink: #1a1a1a;
    --rule: #111111;
  }
  * { margin: 0; padding: 0; box-sizing: border-box; }
  html, body {
    width: 1200px;
    height: 1200px;
    overflow: hidden;
    background: var(--page-bg);
    font-family: "Raleway", sans-serif;
    font-variant-numeric: lining-nums;
    font-feature-settings: "lnum" 1;
    color: var(--ink);
  }
  .canvas { position: relative; width: 1200px; height: 1200px; }

  .card {
    position: absolute;
    left: 173px;
    width: 853px;
    height: 488px;
    background: var(--card-bg);
  }
  .card--front { top: 69px; }
  .card--back { top: 643px; }

  /* Front */
  .brand-mark {
    position: absolute;
    display: flex;
    align-items: center;
    gap: 10px;
    font-weight: 800;
    color: var(--brand-navy);
    white-space: nowrap;
  }
  .card--front .brand-mark { left: 48px; top: 122px; font-size: 36px; }
  .brand-mark__square { background: var(--brand-red); flex: none; }
  .card--front .brand-mark__square { width: 22px; height: 22px; }

  .holder-name {
    position: absolute;
    left: 397px; top: 50px;
    font-size: 38px;
    font-weight: 500;
    color: var(--name-grey);
    white-space: nowrap;
  }
  .holder-title {
    position: absolute;
    left: 397px; top: 96px;
    font-size: 26px;
    font-weight: 500;
  }
  .divider {
    position: absolute;
    left: 397px; top: 145px;
    width: 419px; height: 2px;
    background: var(--rule);
  }
  .contact-list {
    position: absolute;
    left: 397px; top: 162px;
    list-style: none;
    font-size: 24px;
    line-height: 32.5px;
  }
  .contact-list li { white-space: nowrap; }
  .contact-list .email { font-size: 22px; }
  .side-rule {
    position: absolute;
    left: 397px; top: 264px;
    width: 2px; height: 180px;
    background: var(--rule);
  }
  .website {
    position: absolute;
    left: 419px; top: 419px;
    font-size: 22px;
  }
  .address {
    position: absolute;
    left: 50px; top: 316px;
    font-style: normal;
    font-size: 24px;
    line-height: 32.5px;
    white-space: nowrap;
  }

  /* Back */
  .card--back .brand-mark {
    left: 0; right: 0; top: 180px;
    justify-content: center;
    font-size: 66px;
    gap: 18px;
  }
  .card--back .brand-mark__square { width: 38px; height: 38px; }
  .licence-band {
    position: absolute;
    left: 0; bottom: 0;
    width: 100%; height: 83px;
    background: var(--brand-navy);
    color: #ffffff;
    display: flex;
    align-items: center;
    justify-content: center;
    font-size: 24px;
    white-space: pre;
  }
</style>
</head>
<body>
<main class="canvas">

  <section class="card card--front" aria-label="Card front">
    <div class="brand-mark"><span class="brand-mark__square"></span>Vorpelt Pty. Ltd.</div>

    <h1 class="holder-name">Kieran Tolvaris</h1>
    <p class="holder-title">Manager</p>
    <div class="divider"></div>

    <ul class="contact-list">
      <li>P: 0358916047</li>
      <li>F: 0358934268</li>
      <li class="email">kierant@vorpelt.com.au</li>
    </ul>

    <div class="side-rule"></div>
    <p class="website">www.vorpelt.com.au</p>

    <address class="address">
      17 Pellow st<br>
      Tarrawong Vic 3652<br>
      P.o. Box 762<br>
      Tarrawong Vic 3651
    </address>
  </section>

  <section class="card card--back" aria-label="Card back">
    <div class="brand-mark"><span class="brand-mark__square"></span>Vorpelt Pty. Ltd.</div>
    <p class="licence-band">Licence numbers: Vic 27584, NSW 41958K   | |   Solar B3168459</p>
  </section>

</main>
</body>
</html>
```